We would like to incorporate our logo into letterhead design and envelopes. We are looking for something that is moderately conservative but not old law firm style. Both the envelopes and the letterhead must have both firm addresses. We would like to incorporate the color of the logo, but only a small amount of color - perhaps on one of the borders. The addresses for the firm locations are listed below. Given that it is a law firm, it needs to somewhat conservative, but not the old school, small black font on cream colored paper design.

The firm addresses are:

27815 N. Harlow Pemberton Pkwy.
Ste 4200
Scottsdale, AZ 85391

6100 W. Cedar Avenue
Ste 700
Burbank, CA 91623

Industry/Entity Type

Legal

Colors

Designer to choose colors to be used in the design.

Requirements
Must have
• Both addresses:
• 27815 N. Harlow Pemberton Pkwy.
• Ste 4200
• Scottsdale, AZ 85391
• 6100 W. Cedar Avenue
• Ste 700
• Burbank, CA 91623
Nice to have
• Small amount of color on border(s) that matches the logo but not too much color

```html
<!DOCTYPE html>
<html lang="en">
<head>
<meta charset="utf-8">
<title>Calder Vane Law — Stationery</title>
<link rel="stylesheet" href="https://fonts.googleapis.com/css2?family=Marcellus&family=Open+Sans:wght@400&family=Roboto:wght@400;500&display=swap">
<style>
  :root {
    --navy: #29235f;
    --ink: #3a3a3a;
    --paper: #ffffff;
    --backdrop: #a3a3a3;
    --sig-tone: #e6e6e9;
  }
  * { box-sizing: border-box; margin: 0; padding: 0; }
  html, body { width: 1200px; height: 1107px; overflow: hidden; }
  body { background: var(--backdrop); position: relative; font-family: "Open Sans", sans-serif; }

  .sheet-back { position: absolute; left: 139px; top: 214px; width: 553px; height: 782px; background: var(--navy); }

  .letterhead { position: absolute; left: 228px; top: 125px; width: 554px; height: 784px; background: var(--paper); }
  .letterhead__brand {
    position: absolute; top: 38px; left: 0; width: 100%; text-align: center;
    font-family: "Marcellus", serif; font-size: 44px; color: var(--navy); letter-spacing: 0.5px; line-height: 1;
  }
  .letterhead__body {
    position: absolute; left: 54px; top: 160px; width: 453px;
    font-size: 10.6px; line-height: 15.1px; color: var(--ink);
  }
  .letterhead__body p { margin-bottom: 15.1px; text-align: justify; }
  .letterhead__body .salutation, .letterhead__body .closing { text-align: left; }
  .signature { width: 70px; height: 66px; background: var(--sig-tone); margin-top: 6px; }

  .letterhead__footer { position: absolute; left: 49px; top: 696px; width: 458px; font-family: "Roboto", sans-serif; }
  .footer-rule { display: flex; align-items: center; gap: 9px; font-weight: 500; font-size: 12.5px; color: var(--navy); }
  .footer-rule .line { flex: 1; height: 1.2px; background: var(--navy); }
  .footer-addresses { display: flex; justify-content: space-between; font-size: 12.5px; line-height: 15.5px; color: var(--ink); margin-top: 2px; }
  .footer-addresses .right { text-align: right; }

  .card { position: absolute; left: 845px; width: 235px; height: 133px; }
  .card--front { top: 386px; background: var(--navy); display: flex; align-items: center; justify-content: center; }
  .card--front .card__brand { font-family: "Marcellus", serif; font-size: 23px; color: var(--paper); }
  .card--back { top: 581px; background: var(--paper); }
  .card--back .card__brand { position: absolute; top: 13px; width: 100%; text-align: center; font-family: "Marcellus", serif; font-size: 17px; color: var(--navy); }
  .card__person { position: absolute; left: 17px; top: 52px; font-family: "Roboto", sans-serif; color: var(--ink); }
  .card__name { font-family: "Marcellus", serif; font-size: 8px; letter-spacing: 0.3px; color: #1f1f2e; }
  .card__title { font-size: 6px; }
  .card__dash { width: 10px; height: 1px; background: var(--navy); margin: 3px 0 5px; }
  .card__lines { font-size: 5.2px; line-height: 7.4px; }
  .card__lines .icon-row { display: flex; align-items: center; gap: 2px; }
  .card__lines svg { width: 5px; height: 5px; fill: var(--navy); }
  .card__second { position: absolute; right: 17px; top: 104px; text-align: right; font-family: "Roboto", sans-serif; font-size: 5.2px; line-height: 7.4px; color: var(--ink); }
</style>
</head>
<body>
  <div class="sheet-back"></div>

  <section class="letterhead">
    <div class="letterhead__brand">CALDER VANE LAW</div>
    <div class="letterhead__body">
      <p class="salutation">Dear customer,</p>
      <p>Lorem ipsum dolor sit amet, consectetur adipisicing elit, sed do eiusmod tempor incididunt ut labore et dolore magna aliqua. Ut enim ad minim veniam, quis nostrud exercitation ullamco laboris nisi ut aliquip ex ea commodo consequat. Duis aute irure dolor in reprehenderit in voluptate velit esse cillum dolore eu fugiat nulla pariatur. Excepteur sint occaecat cupidatat non proident, sunt in culpa qui officia deserunt mollit anim id est laborum.</p>
      <p>Lorem ipsum dolor sit amet, consectetur adipisicing elit, sed do eiusmod tempor incididunt ut labore et dolore magna aliqua. Ut enim ad minim veniam, quis nostrud exercitation ullamco laboris nisi ut aliquip ex ea commodo consequat. Duis aute irure dolor in reprehenderit in voluptate velit esse cillum dolore eu fugiat nulla pariatur. Excepteur sint occaecat cupidatat non proident, sunt in culpa qui officia deserunt mollit anim id est laborum.</p>
      <p>Lorem ipsum dolor sit amet, consectetur adipisicing elit, sed do eiusmod tempor incididunt ut labore et dolore magna aliqua. Ut enim ad minim veniam, quis nostrud exercitation ullamco laboris nisi ut aliquip ex ea commodo consequat. Duis aute irure dolor in reprehenderit in voluptate velit esse cillum dolore eu fugiat nulla pariatur. Excepteur sint occaecat cupidatat non proident, sunt in culpa qui officia deserunt mollit anim id est laborum.</p>
      <p>Lorem ipsum dolor sit amet, consectetur adipisicing elit, sed do eiusmod tempor incididunt ut labore et dolore magna aliqua. Ut enim ad minim veniam, quis nostrud exercitation ullamco laboris nisi ut aliquip ex ea commodo consequat. Duis aute irure dolor in reprehenderit.</p>
      <p class="closing">Yours Sincerely,</p>
      <div class="signature" role="img" aria-label="Handwritten signature of the sender"></div>
    </div>
    <footer class="letterhead__footer">
      <div class="footer-rule"><span>Address :</span><span class="line"></span><span>Address:</span></div>
      <div class="footer-addresses">
        <div class="left">27815 N. Harlow Pemberton Pkwy.<br>Ste 4200 Scottsdale, AZ 85391</div>
        <div class="right">6100 W. Cedar Avenue<br>Ste 700 Burbank, CA 91623</div>
      </div>
    </footer>
  </section>

  <section class="card card--front">
    <div class="card__brand">CALDER VANE LAW</div>
  </section>

  <section class="card card--back">
    <div class="card__brand">CALDER VANE LAW</div>
    <div class="card__person">
      <div class="card__name">DANIEL ASHFORD</div>
      <div class="card__title">President</div>
      <div class="card__dash"></div>
      <div class="card__lines">
        <div>27815 N. Harlow Pemberton Pkwy.</div>
        <div>Ste 4200 Scottsdale, AZ 85391</div>
        <div class="icon-row"><svg viewBox="0 0 10 10"><path d="M2 1l2 2-1 1.5c.6 1.2 1.4 2 2.5 2.5L7 6l2 2-1.5 1.5C4.5 9 1 5.5.5 2.5z"/></svg>0400 555 018</div>
        <div class="icon-row"><svg viewBox="0 0 10 10"><path d="M0 2h10v6H0zM.8 2.6L5 5.6l4.2-3v.8L5 6.4.8 3.4z"/></svg>daniel@caldervanelaw.com.au</div>
        <div class="icon-row"><svg viewBox="0 0 10 10"><circle cx="5" cy="5" r="4.5"/></svg>www.caldervanelaw.com.au</div>
      </div>
    </div>
    <div class="card__second">6100 W. Cedar Avenue<br>Ste 700 Burbank, CA 91623</div>
  </section>
</body>
</html>
```